Design of two graphics from basic existing design & colours

I have two graphics which I currently use but they are nothing special. We would like to transform these two graphics, using our existing logo colour, into something special. The outputs will be used:

- on our website;
- in a powerpoint sales presentation;
- in email campaigns; and
- to print for handing to prospects at the end of a sales presentation.

Please just submit one of the graphics and if we like the design, we will ask you to work on the second graphic. These two graphics are critical to our marketing and will be used together so we need them to have a similar look and feel.

```html
<!DOCTYPE html>
<html lang="en">
<head>
<meta charset="utf-8">
<title>Governance System</title>
<link rel="stylesheet" href="https://fonts.googleapis.com/css2?family=Arimo:wght@400;700&display=swap">
<style>
  :root {
    --title: #6b2a1e;
    --strategic-head: #4a1611;
    --strategic-body: #5f1e15;
    --financial-head: #a22a21;
    --financial-body: #c74234;
    --operational-head: #a8302a;
    --operational-body: #d5604a;
    --cultural-head: #3a3a3a;
    --cultural-body: #a6a6a6;
    --band-brown: #5a271e;
    --band-red: #c4402f;
    --band-black: #1e1a1a;
    --paper: #ffffff;
    --ink-light: #ffffff;
  }
  html, body {
    margin: 0;
    padding: 0;
    width: 1200px;
    height: 675px;
    overflow: hidden;
    background: var(--paper);
  }
  .canvas {
    display: block;
    width: 1200px;
    height: 675px;
    font-family: "Arimo", Arial, sans-serif;
  }
  .title { fill: var(--title); font-weight: 700; font-size: 24px; }
  .hex-label { fill: var(--ink-light); font-weight: 700; font-size: 21px; text-anchor: middle; }
  .hex-item { fill: var(--ink-light); font-size: 14px; }
  .hex-item--small { font-size: 12.5px; }
  .strategic-head { fill: var(--strategic-head); }
  .strategic-body { fill: var(--strategic-body); }
  .financial-head { fill: var(--financial-head); }
  .financial-body { fill: var(--financial-body); }
  .operational-head { fill: var(--operational-head); }
  .operational-body { fill: var(--operational-body); }
  .cultural-head { fill: var(--cultural-head); }
  .cultural-body { fill: var(--cultural-body); }
  .hex-shape { stroke: var(--paper); stroke-width: 3; stroke-linejoin: round; }
  .band-brown { fill: var(--band-brown); }
  .band-red { fill: var(--band-red); }
  .band-black { fill: var(--band-black); }
  .brand-name { fill: var(--title); font-weight: 700; font-size: 15px; letter-spacing: 0.5px; }
</style>
</head>
<body>
<svg class="canvas" viewBox="0 0 960 540" xmlns="http://www.w3.org/2000/svg" role="img" aria-label="Governance System diagram">
  <defs>
    <filter id="soft-shadow" x="-10%" y="-10%" width="120%" height="130%">
      <feDropShadow dx="0" dy="2" stdDeviation="2" flood-color="#000" flood-opacity="0.25"/>
    </filter>
  </defs>

  <text class="title" x="82" y="81">Governance</text>
  <text class="title" x="82" y="112">System</text>

  <!-- Strategic -->
  <g class="hex hex--strategic" filter="url(#soft-shadow)">
    <polygon class="hex-shape strategic-head" points="490,52 630,52 655,97 465,97"/>
    <polygon class="hex-shape strategic-body" points="463,100 657,100 685,147 630,242 490,242 435,147"/>
  </g>
  <text class="hex-label" x="560" y="81">Strategic</text>
  <text class="hex-item" x="480" y="140">• Board</text>
  <text class="hex-item" x="480" y="158">• Purpose</text>
  <text class="hex-item" x="480" y="176">• Risk</text>
  <text class="hex-item" x="480" y="194">• Strategy</text>
  <text class="hex-item" x="574" y="140">• Structure</text>
  <text class="hex-item" x="574" y="158">• Values</text>
  <text class="hex-item" x="574" y="176">• Vision</text>

  <!-- Financial -->
  <g class="hex hex--financial" filter="url(#soft-shadow)">
    <polygon class="hex-shape financial-head" points="288,157 424,157 449,201 263,201"/>
    <polygon class="hex-shape financial-body" points="261,204 451,204 478,251 424,345 288,345 234,251"/>
  </g>
  <text class="hex-label" x="356" y="186">Financial</text>
  <text class="hex-item" x="266" y="250">• Budget</text>
  <text class="hex-item" x="266" y="268">• CAPEX</text>
  <text class="hex-item" x="266" y="286">• Cash Flow</text>
  <text class="hex-item" x="360" y="250">• Delegations</text>
  <text class="hex-item" x="360" y="268">• OPEX</text>

  <!-- Operational -->
  <g class="hex hex--operational" filter="url(#soft-shadow)">
    <polygon class="hex-shape operational-head" points="704,157 840,157 865,201 679,201"/>
    <polygon class="hex-shape operational-body" points="677,204 867,204 895,251 840,345 704,345 650,251"/>
  </g>
  <text class="hex-label" x="772" y="186">Operational</text>
  <text class="hex-item" x="684" y="238">• Competitor</text>
  <text class="hex-item" x="684" y="256">• Compliance</text>
  <text class="hex-item" x="684" y="274">• Customer</text>
  <text class="hex-item" x="684" y="292">• Marketing</text>
  <text class="hex-item" x="684" y="310">• Meetings</text>
  <text class="hex-item" x="784" y="240">• Planning</text>
  <text class="hex-item" x="784" y="258">• Policy</text>
  <text class="hex-item" x="784" y="276">• Projects</text>
  <text class="hex-item" x="784" y="294">• Reporting</text>
  <text class="hex-item" x="784" y="312">• Review</text>

  <!-- Cultural -->
  <g class="hex hex--cultural" filter="url(#soft-shadow)">
    <polygon class="hex-shape cultural-head" points="497,252 631,252 656,297 472,297"/>
    <polygon class="hex-shape cultural-body" points="470,300 658,300 685,345 631,438 497,438 443,345"/>
  </g>
  <text class="hex-label" x="564" y="282">Cultural</text>
  <text class="hex-item hex-item--small" x="468" y="328">• Coaching</text>
  <text class="hex-item hex-item--small" x="468" y="345">• Communication</text>
  <text class="hex-item hex-item--small" x="468" y="362">• Competencies</text>
  <text class="hex-item hex-item--small" x="468" y="379">• Development</text>
  <text class="hex-item hex-item--small" x="468" y="396">• Employment</text>
  <text class="hex-item hex-item--small" x="581" y="328">• Leadership</text>
  <text class="hex-item hex-item--small" x="581" y="345">• Performance</text>
  <text class="hex-item hex-item--small" x="581" y="362">• Profiles</text>
  <text class="hex-item hex-item--small" x="581" y="379">• Succession</text>
  <text class="hex-item hex-item--small" x="581" y="396">• Teams</text>

  <!-- Footer bands -->
  <polygon class="band-brown" points="205,487 545,487 512,540 172,540"/>
  <polygon class="band-red" points="545,487 785,487 752,540 512,540"/>
  <polygon class="band-black" points="785,487 960,487 960,540 752,540"/>

  <!-- Brand -->
  <text class="brand-name" x="40" y="518">Meridian Advisory</text>
</svg>
</body>
</html>
```